K&T Fixit and Rebuild general contracting business card design

I already have a logo that I want to use and I need a card that uses that logo and color scheme on the front with the address phone numbers and email and on the back a place for technicians to write in their name and phone number when they hand it out. It will need the License number of License #KTFXTRB318QN.
It should say General Contractor under the company name. The address is
4417 NE 3rd Ave, Ste D246
Vancouver, WA 98612
www.kandtfixitandrebuild.example
office@kandtfixitandrebuild.example
360-555-0182 is the telephone number
360-555-0149 is the fax number

Target Market(s)

Homeowners needing remodel work or repairs in their home.

Industry/Entity Type

Construction

Contact Information for Business Card

Business name, address, phone number, license number, fax number, email, and website on the front and a place to fill in technician's name and number

Font styles to use
Serif

Requirements
Must have
• Business name, address, phone number, license number, fax number, email, and website on the front and a place to fill in technician's name and number
Nice to have
• I uploaded an example of a front that is good.
Should not have
• Froo froo or extra embellishments.

```html
<!DOCTYPE html>
<html lang="en">
<head>
<meta charset="utf-8">
<title>K&amp;T Fixit and Rebuild — Business Card</title>
<link href="https://fonts.googleapis.com/css2?family=Poppins:wght@400;500;600&display=swap" rel="stylesheet">
<style>
  :root {
    --backdrop: #97cbf7;
    --paper: #ffffff;
    --ink: #1f1f1f;
    --wood-light: #8a5428;
    --wood-mid: #7a4a22;
    --wood-dark: #6a3d19;
    --badge: #2e1510;
    --tan: #d89a76;
    --tan-faint: #f0ddd3;
    --cream: #ffffff;
  }
  * { margin: 0; padding: 0; box-sizing: border-box; }
  html, body {
    width: 1200px; height: 1200px; overflow: hidden;
    background: var(--backdrop);
    font-family: "Poppins", sans-serif;
  }
  .card {
    position: absolute; left: 180px; width: 840px; height: 480px;
    box-shadow: 0 4px 14px rgba(40, 90, 140, 0.25);
    overflow: hidden;
  }
  .card--back { top: 82px; background: var(--paper); }
  .card--front { top: 638px; }

  .watermark {
    position: absolute; left: 476px; width: 300px; z-index: 0;
    text-align: center; color: var(--tan-faint);
  }
  .watermark__name { top: 232px; font-size: 32px; font-weight: 600; line-height: 1.15; }
  .watermark__tagline { top: 330px; font-size: 20px; font-weight: 600; letter-spacing: 1px; text-transform: uppercase; }

  .fill-field {
    position: absolute; left: 88px; right: 88px; z-index: 1;
    display: flex; align-items: flex-end; gap: 10px;
    font-size: 24px; color: var(--ink);
  }
  .fill-field__line { flex: 1; border-bottom: 2px solid var(--ink); height: 0; margin-bottom: 6px; }
  .fill-field--name { top: 182px; }
  .fill-field--phone { top: 284px; }

  .wood {
    position: absolute; inset: 0;
    background: linear-gradient(180deg, var(--wood-mid) 0%, var(--wood-light) 45%, var(--wood-dark) 100%);
  }
  .badge {
    position: absolute; left: 44px; top: 118px; width: 244px; height: 244px;
    border-radius: 50%; background: var(--badge);
    display: flex; flex-direction: column; align-items: center; justify-content: center; text-align: center;
    color: var(--tan); padding: 0 26px;
  }
  .badge__name { font-size: 26px; font-weight: 600; line-height: 1.2; }
  .badge__tagline { margin-top: 8px; font-size: 13px; font-weight: 500; letter-spacing: 1.5px; text-transform: uppercase; }

  .contact { position: absolute; left: 318px; top: 108px; color: var(--cream); font-size: 24px; line-height: 1.2; }
  .contact__row { display: flex; align-items: flex-start; gap: 14px; margin-bottom: 10px; }
  .contact__icon {
    flex: none; width: 30px; height: 30px; border-radius: 50%; background: var(--badge);
    display: flex; align-items: center; justify-content: center;
  }
  .contact__icon svg { width: 17px; height: 17px; fill: none; stroke: var(--tan); stroke-width: 2; stroke-linecap: round; stroke-linejoin: round; }
  .contact__license { margin-left: 44px; }
</style>
</head>
<body>

<section class="card card--back">
  <div class="watermark watermark__name">K&amp;T Fixit and Rebuild</div>
  <div class="watermark watermark__tagline">General Contractor</div>
  <div class="fill-field fill-field--name"><span>Name:</span><span class="fill-field__line"></span></div>
  <div class="fill-field fill-field--phone"><span>Phone:</span><span class="fill-field__line"></span></div>
</section>

<section class="card card--front">
  <div class="wood" role="img" aria-label="Vertical wooden plank texture background"></div>
  <div class="badge">
    <div class="badge__name">K&amp;T Fixit and Rebuild</div>
    <div class="badge__tagline">General Contractor</div>
  </div>

  <div class="contact">
    <div class="contact__row">
      <span class="contact__icon"><svg viewBox="0 0 24 24"><path d="M12 22s7-7 7-12a7 7 0 0 0-14 0c0 5 7 12 7 12z"/><circle cx="12" cy="10" r="2.5"/></svg></span>
      <span>4417 NE 3rd Ave, Ste D246<br>Vancouver, WA 98612</span>
    </div>
    <div class="contact__row">
      <span class="contact__icon"><svg viewBox="0 0 24 24"><circle cx="12" cy="12" r="9"/><path d="M3 12h18M12 3c3 3 3 15 0 18M12 3c-3 3-3 15 0 18"/></svg></span>
      <span>kandtfixitandrebuild.example</span>
    </div>
    <div class="contact__row">
      <span class="contact__icon"><svg viewBox="0 0 24 24"><rect x="3" y="6" width="18" height="12" rx="1"/><path d="M3 7l9 6 9-6"/></svg></span>
      <span>office@kandtfixitandrebuild.example</span>
    </div>
    <div class="contact__row">
      <span class="contact__icon"><svg viewBox="0 0 24 24"><path d="M5 4h4l2 5-2.5 1.5a11 11 0 0 0 5 5L15 13l5 2v4a2 2 0 0 1-2 2A16 16 0 0 1 3 6a2 2 0 0 1 2-2z"/></svg></span>
      <span>360-555-0182</span>
    </div>
    <div class="contact__row">
      <span class="contact__icon"><svg viewBox="0 0 24 24"><path d="M7 9V3h10v6"/><rect x="3" y="9" width="18" height="8" rx="1"/><rect x="7" y="14" width="10" height="7"/></svg></span>
      <span>360-555-0149</span>
    </div>
    <div class="contact__license">License #KTFXTRB318QN</div>
  </div>
</section>

</body>
</html>
```